Business Card Re-Design

Consulting Company: To build a high performance organization, you need great leaders at all levels throughout your organization. The Northvale Talent Growth Studio engages, inspires, and educates current and future leaders to step beyond the ordinary and deliver exceptional results. This new breed of leaders will motivate your staff to leave the safety of complacency behind and come together to build an extraordinary organization. The current trend has been to ask our people to do more with fewer resources. People have been stepping up to the challenge, but more is required to ensure success with a new work paradigm. We work with your management team to build a successful strategy that will make your organization more effective. NTGS then supports your management team by providing a comprehensive set of proven services to empower your entire organization to successfully execute new strategies.Let NTGS help you optimize your organization’s individual and team performance today!

Target Market(s)

Federal, State and Local Government / Non profit

Industry/Entity Type

Management Consulting

Contact Information for Business Card

NTGS, inc (Northvale Talent Growth Studio) Optimizing Individual and Organizational Performance

Colors
fee18a
ec1f27
474747
fbf289

Requirements
Must have
• Professional and high quality feel

```html
<!DOCTYPE html>
<html lang="en">
<head>
<meta charset="utf-8">
<title>Northvale Talent Growth Studio — Business Card</title>
<link rel="stylesheet" href="https://fonts.googleapis.com/css2?family=Libre+Bodoni:wght@500;700&family=Arimo:wght@400&display=swap">
<style>
  :root {
    --backdrop: #d9d2c8;
    --card-cream: #f4f1ea;
    --card-black: #0c0c0c;
    --accent-red: #c8202a;
    --gold: #c2a93f;
    --ink-brown: #3b2a1b;
    --soft-white: #e9e6df;
    --divider: #d8d4cc;
  }
  html, body {
    margin: 0;
    width: 1200px;
    height: 823px;
    overflow: hidden;
    background: var(--backdrop);
  }
  .canvas {
    position: relative;
    width: 1200px;
    height: 823px;
  }
  .business-card {
    position: absolute;
    left: 100px;
    top: 125px;
    width: 1000px;
    height: 572px;
    background: var(--card-cream);
    box-shadow: 0 10px 30px rgba(0,0,0,0.18);
    overflow: hidden;
  }
  .card-shapes {
    position: absolute;
    inset: 0;
  }
  .brand {
    position: absolute;
    left: 0;
    width: 960px;
    top: 40px;
    text-align: center;
  }
  .brand-mark {
    display: block;
    margin: 0 auto 22px;
  }
  .brand-name {
    margin: 0;
    font-family: "Libre Bodoni", serif;
    font-weight: 700;
    font-size: 40px;
    line-height: 1.15;
    letter-spacing: 1px;
    color: var(--ink-brown);
  }
  .person {
    position: absolute;
    left: 70px;
    top: 450px;
  }
  .person-name {
    margin: 0;
    font-family: "Libre Bodoni", serif;
    font-weight: 700;
    font-size: 38px;
    color: var(--gold);
  }
  .person-title {
    margin: 4px 0 0;
    font-family: "Libre Bodoni", serif;
    font-weight: 700;
    font-size: 21px;
    color: var(--soft-white);
  }
  .divider {
    position: absolute;
    left: 560px;
    top: 420px;
    width: 2px;
    height: 135px;
    background: var(--divider);
  }
  .contact-list {
    position: absolute;
    left: 592px;
    top: 412px;
    margin: 0;
    padding: 0;
    list-style: none;
    font-family: "Arimo", sans-serif;
    font-size: 17px;
    color: var(--soft-white);
  }
  .contact-item {
    display: flex;
    align-items: center;
    height: 28px;
  }
  .contact-icon {
    width: 11px;
    height: 11px;
    margin-right: 14px;
    background: var(--gold);
    border-radius: 2px;
    flex: none;
  }
</style>
</head>
<body>
<div class="canvas">
  <div class="business-card">
    <svg class="card-shapes" width="1000" height="572" viewBox="0 0 1000 572" aria-hidden="true">
      <path class="black-panel" d="M0,330 C200,470 650,470 1000,80 L1000,572 L0,572 Z" fill="var(--card-black)"/>
      <path class="red-swoosh" d="M0,330 C200,458 650,456 1000,80 C650,470 200,470 0,330 Z" fill="var(--accent-red)"/>
    </svg>

    <div class="brand">
      <svg class="brand-mark" width="90" height="90" viewBox="0 0 90 90" aria-hidden="true">
        <circle cx="45" cy="45" r="42" fill="none" stroke="var(--ink-brown)" stroke-width="3"/>
      </svg>
      <p class="brand-name">Northvale Talent<br>Growth Studio</p>
    </div>

    <div class="person">
      <p class="person-name">Marcus L. Whitfield</p>
      <p class="person-title">President &amp; CEO</p>
    </div>

    <div class="divider"></div>

    <ul class="contact-list">
      <li class="contact-item"><span class="contact-icon"></span>555-014-2083</li>
      <li class="contact-item"><span class="contact-icon"></span>555-014-7791</li>
      <li class="contact-item"><span class="contact-icon"></span>mwhitfield@ntgsinc.com</li>
      <li class="contact-item"><span class="contact-icon"></span>www.ntgsinc.com</li>
      <li class="contact-item"><span class="contact-icon"></span>PO Box 4180 Easton, MD 21601</li>
    </ul>
  </div>
</div>
</body>
</html>
```